50 Lessons from my entrepreneurial journey

make a book cover (see attached file for reference or sample )
https://files.plumvault.example/d/7kQwErtY9uIoPzXcVbNm3aSdFgH4jKl2L/view?usp=share_link

make a back book cover (see writings below)

BUILD A BUSINESS. BUILD A LIFE.

What does it really take to succeed, not just in business, but in life?

In MARLO’S LEDGER, award-winning entrepreneur, speaker, and columnist Marlo Vintrell shares 50 powerful lessons and more drawn from over three decades of building Cebu’s most beloved homegrown brands. Honest, practical, and deeply personal, this book brings together timeless insights on entrepreneurship, leadership, family, faith, and the inner journey of growth.

Whether you’re just starting out, scaling up, or searching for clarity in the next chapter of your life, these pages will guide, inspire, and challenge you to pursue something greater not just profit, but purpose. More than a business book, this is a book about building the kind of life you won’t need a vacation from.

About the Author

Marlo Vintrell is one of Cebu’s most respected and successful entrepreneurs, best known for building iconic homegrown brands such as Breezy Blends and Smoothies, Hall of Roastfire, and The Crestline Deck. As Chairman and CEO of the Vintrell Food Group, he has spent over 25 years shaping the business landscape of the Visayas and Mindanao. Named Entrepreneur of the Year by the Korvand Guild of Trade and Enterprise and recognized for one of the Top Ten Most Outstanding Family Businesses in the Philippines, Marlo is also a popular columnist for DawnPost Vesta. Through his writing and mentorship, he continues to empower the next generation to build with heart, lead with purpose, and live with meaning.

Target Market(s)

Millennials & Young Professionals

Industry/Entity Type

Entrepreneurship

Font styles to use
Serif
Sans Serif

Requirements
Must have
• Professional yet clean modern typography

```html
<!DOCTYPE html>
<html lang="en">
<head>
<meta charset="utf-8">
<title>50 Lessons from My Entrepreneurial Journey – Book Cover</title>
<link href="https://fonts.googleapis.com/css2?family=Anton&family=Montserrat:wght@400;500&display=swap" rel="stylesheet">
<style>
  :root {
    --backdrop: #a6a6a6;
    --ink: #000000;
    --paper: #ffffff;
    --photo-light: #e9e7e4;
    --photo-dark: #3a3a3c;
    --display: "Anton", "Oswald", sans-serif;
    --text: "Montserrat", "Helvetica Neue", Arial, sans-serif;
  }
  * { margin: 0; padding: 0; box-sizing: border-box; }
  html, body { width: 1200px; height: 1200px; overflow: hidden; }
  body { background: var(--backdrop); position: relative; }

  .spread {
    position: absolute; left: 51px; top: 207px;
    width: 1098px; height: 785px;
    box-shadow: 0 0 2px rgba(0,0,0,.35);
  }

  /* Back cover */
  .back-cover {
    position: absolute; left: 0; top: 0; width: 523px; height: 785px;
    background: var(--ink); color: var(--paper);
  }
  .back-title {
    position: absolute; left: 0; right: 0; top: 36px;
    text-align: center; font-family: var(--display); font-weight: 400;
    font-size: 31px; line-height: 38px; letter-spacing: 0;
  }
  .back-title .light { font-family: var(--text); font-weight: 500; font-size: 23px; }
  .blurb {
    position: absolute; left: 29px; width: 465px;
    font-family: var(--text); font-size: 11.7px; line-height: 19.4px;
    text-align: justify;
  }
  .blurb-one { top: 122px; }
  .blurb-two { top: 232px; }
  .author {
    position: absolute; left: 29px; top: 349px; width: 465px;
    font-family: var(--text); font-size: 11.7px; line-height: 19.4px; text-align: justify;
  }
  .author-photo {
    float: left; width: 111px; height: 129px; margin: 0 11px 4px 0;
    background: var(--paper); border-radius: 12px;
  }
  .author-name {
    font-family: var(--display); font-weight: 400; font-size: 30px; line-height: 34px;
    letter-spacing: 2.5px; margin: -2px 0 2px;
  }
  .code-box {
    position: absolute; left: 339px; top: 675px; width: 155px; height: 73px;
    background: var(--paper);
  }

  /* Spine */
  .spine {
    position: absolute; left: 523px; top: 0; width: 52px; height: 785px;
    background: var(--paper);
  }

  /* Front cover */
  .front-cover {
    position: absolute; left: 575px; top: 0; width: 523px; height: 785px;
    background: var(--paper);
  }
  .front-band-top { position: absolute; left: 0; top: 0; width: 523px; height: 279px; background: var(--ink); }
  .front-band-bottom { position: absolute; left: 0; bottom: 0; width: 523px; height: 87px; background: var(--ink); }
  .author-portrait {
    position: absolute; left: 133px; top: 308px; width: 360px; height: 390px;
    border-radius: 110px 110px 0 0;
    background: linear-gradient(180deg, var(--photo-light) 0%, #bdb7b1 30%, var(--photo-dark) 55%, #1f1f21 100%);
  }
  .front-art { position: absolute; left: 0; top: 0; }
</style>
</head>
<body>
<div class="spread">

  <section class="back-cover">
    <h2 class="back-title">50 LESSONS <span class="light">FROM MY</span><br>ENTREPRENEURIAL JOURNEY</h2>
    <p class="blurb blurb-one">In MARLO’S LEDGER, award-winning entrepreneur, speaker, and columnist Marlo Vintrell shares 50 powerful lessons and more drawn from over three decades of building Cebu’s most beloved homegrown brands. Honest, practical, and deeply personal, this book brings together timeless insights on entrepreneurship, leadership, family, faith, and the inner journey of growth.</p>
    <p class="blurb blurb-two">Whether you’re just starting out, scaling up, or searching for clarity in the next chapter of your life, these pages will guide, inspire, and challenge you to pursue something greater not just profit, but purpose. More than a business book, this is a book about building the kind of life you won’t need a vacation from.</p>
    <div class="author">
      <div class="author-photo" role="img" aria-label="Author photo placeholder"></div>
      <h3 class="author-name">MARLO VINTRELL</h3>
      <p>Marlo Vintrell is one of Cebu’s most respected and successful entrepreneurs, best known for building iconic homegrown brands such as Breezy Blends and Smoothies, Hall of Roastfire, and The Crestline Deck. As Chairman and CEO of the Vintrell Food Group, he has spent over 25 years shaping the business landscape of the Visayas and Mindanao. Named Entrepreneur of the Year by the Korvand Guild of Trade and Enterprise and recognized for one of the Top Ten Most Outstanding Family Businesses in the Philippines, Marlo is also a popular columnist for DawnPost Vesta. Through his writing and mentorship, he continues to empower the next generation to build with heart, lead with purpose, and live with meaning.</p>
    </div>
    <div class="code-box"></div>
  </section>

  <section class="spine">
    <svg width="52" height="785" viewBox="0 0 52 785">
      <g transform="translate(16 36) rotate(90)" fill="#000">
        <text x="0" y="0" font-family="Anton, sans-serif" font-size="27" textLength="471" lengthAdjust="spacingAndGlyphs">50 LESSONS <tspan font-family="Montserrat, sans-serif" font-weight="500" font-size="22">FROM MY</tspan> ENTREPRENEURIAL JOURNEY</text>
        <text x="555" y="0" font-family="Anton, sans-serif" font-size="27" letter-spacing="4" textLength="155" lengthAdjust="spacingAndGlyphs">MARLO VINTRELL</text>
      </g>
    </svg>
  </section>

  <section class="front-cover">
    <div class="front-band-top"></div>
    <div class="author-portrait" role="img" aria-label="Portrait of the author in a dark suit and white shirt"></div>
    <div class="front-band-bottom"></div>
    <svg class="front-art" width="523" height="785" viewBox="0 0 523 785">
      <defs>
        <clipPath id="upper-half"><rect x="0" y="0" width="523" height="279"/></clipPath>
        <clipPath id="lower-half"><rect x="0" y="279" width="523" height="100"/></clipPath>
      </defs>
      <g font-family="Anton, sans-serif" fill="#fff">
        <text x="120" y="108" font-size="96" textLength="384" lengthAdjust="spacingAndGlyphs">50 LESSONS</text>
        <text x="237" y="148" font-family="Montserrat, sans-serif" font-weight="500" font-size="36" textLength="175" lengthAdjust="spacingAndGlyphs">FROM MY</text>
        <text x="120" y="213" font-size="66" textLength="385" lengthAdjust="spacingAndGlyphs">ENTREPRENEURIAL</text>
      </g>
      <text clip-path="url(#upper-half)" x="120" y="332" font-family="Anton, sans-serif" font-size="128" fill="#fff" textLength="384" lengthAdjust="spacingAndGlyphs">JOURNEY</text>
      <text clip-path="url(#lower-half)" x="120" y="332" font-family="Anton, sans-serif" font-size="128" fill="#000" textLength="384" lengthAdjust="spacingAndGlyphs">JOURNEY</text>
      <g font-family="Anton, sans-serif" font-size="30" fill="#000" text-anchor="middle">
        <text x="441" y="392">BUILD A</text>
        <text x="441" y="423">BUSINESS.</text>
        <text x="441" y="455">BUILD A LIFE</text>
      </g>
      <text x="262" y="765" text-anchor="middle" font-family="Anton, sans-serif" font-size="52" fill="#fff" letter-spacing="5" textLength="307" lengthAdjust="spacingAndGlyphs">MARLO VINTRELL</text>
    </svg>
  </section>

</div>
</body>
</html>
```